Pelora Vantu Child Care Website

Website designs are required for a new, modern and state of the art Child Care Centre.

Pelora Vantu Child Care is a new Child Care and Long Day Care provider. It provides care, learning and education services for children under 24 months, toddlers and also preschool children.

The website design needs to incorporate elements of care, fun and learning, while displaying the Brand name clearly - i.e easy to read and understand - considering the unusual name...

We would like to see proposals that focus on portraying a professional overall brand identity. It needs to be modern and use fresh colors.

Please see attached logo concept selected.

***NOTE*** Feel free to adjust colors of this logo based on the site theme.

If you require any clarification please feel free to contact us.

Target Market(s)

School teachers
Parents
Parents with young children

Industry/Entity Type

Education

Requirements
Must have
• Responsive design - must support all browsers
Modern and creative - must make use of modern design techniques. See http://dravenmixo.example/ for inspiration!
Should not have
• copied ideas. keep it original

```html
<!DOCTYPE html>
<html lang="en">
<head>
<meta charset="utf-8">
<title>Pelora Vantu Child Care</title>
<link href="https://fonts.googleapis.com/css2?family=Open+Sans:wght@400;600;700&display=swap" rel="stylesheet">
<style>
:root{
  --orange:#e8781e;
  --charcoal:#333333;
  --charcoal-soft:#3d3a38;
  --frame:#3a3533;
  --mist:#ececec;
  --ink:#2a2a2a;
  --body:#444444;
  --white:#ffffff;
}
*{margin:0;padding:0;box-sizing:border-box}
html,body{width:1200px;height:2687px;overflow:hidden}
body{position:relative;font-family:"Open Sans",Arial,sans-serif;color:var(--body);background:var(--white)}
.abs{position:absolute}

/* hero */
.hero{left:0;top:0;width:1200px;height:721px;background:linear-gradient(160deg,#6d8a4a 0%,#b98a6c 30%,#a73a34 55%,#c9a68c 75%,#3f7d87 100%)}
.hero-shade{left:0;top:0;width:1200px;height:250px;background:rgba(40,34,32,.55)}
.brand{left:0;top:58px;width:1200px;text-align:center;font-weight:700;font-size:44px;line-height:1.1;color:var(--orange)}
.brand small{display:block;font-size:22px;letter-spacing:3px}
.nav{left:96px;top:190px;width:1010px;height:60px}
.nav a{position:absolute;top:0;height:60px;line-height:60px;color:var(--white);font-size:17px;text-decoration:none;transform:translateX(-50%);white-space:nowrap}
.nav a.current{width:117px;text-align:center;border:2px solid var(--orange);line-height:56px}

.showcase{left:188px;top:537px;width:811px;height:385px;background:var(--frame)}
.photo{position:absolute}
.lead-photo{left:25px;top:20px;width:369px;height:343px;background:linear-gradient(150deg,#d9d0c4,#b08b6a 60%,#8aa0b8)}
.lead-photo p{position:absolute;left:18px;bottom:30px;color:var(--white);font-size:22px;font-weight:700;line-height:1.35}
.tile{width:179px;height:161px}
.tile span{position:absolute;left:0;bottom:0;width:100%;height:34px;line-height:34px;text-align:center;color:var(--white);font-weight:700;font-size:17px}
.t1{left:410px;top:20px;background:linear-gradient(160deg,#c7a47f,#8d6b4d)}
.t1 span{background:rgba(111,178,58,.92)}
.t2{left:612px;top:20px;background:linear-gradient(160deg,#d6b091,#a05a3c)}
.t2 span{background:rgba(232,120,30,.92)}
.t3{left:410px;top:202px;background:linear-gradient(160deg,#d8c2a8,#6f8a9c)}
.t3 span{background:rgba(233,194,26,.92)}
.t4{left:612px;top:202px;background:linear-gradient(160deg,#e8c89a,#7fb4d4)}
.t4 span{background:rgba(45,159,216,.92)}

/* welcome */
.welcome-title{left:96px;top:972px;font-size:24px;font-weight:600;color:var(--ink)}
.welcome-text{left:96px;top:1026px;width:702px;font-size:12.5px;line-height:21px;text-align:justify}
.btn-dark{background:var(--charcoal);color:var(--white);font-size:12px;font-weight:600;text-align:center;text-transform:uppercase}
.welcome-btn{left:96px;top:1191px;width:90px;height:38px;line-height:38px}
.welcome-photo{left:828px;top:951px;width:336px;height:292px;background:radial-gradient(ellipse at 55% 55%,#e7c08a 0%,#b8c9d8 45%,#ffffff 75%)}

/* programs */
.programs{left:0;top:1276px;width:1200px;height:439px;background:var(--orange)}
.section-title{font-size:24px;font-weight:600;text-transform:uppercase}
.programs .section-title{position:absolute;left:96px;top:20px;color:var(--white)}
.prog{position:absolute;top:84px;width:240px;transform:translateX(-50%);text-align:center;color:var(--white)}
.prog:before{content:"";display:block;width:100px;height:2px;background:rgba(255,255,255,.6);margin:0 auto 10px}
.prog h3{font-size:15px;font-weight:600;height:30px}
.prog .pic{width:124px;height:124px;margin:8px auto 0;border-radius:50%;border:5px solid var(--white);box-shadow:0 0 0 2px #4a3a30}
.prog p{font-size:10.5px;line-height:17px;margin-top:10px;height:110px}
.prog .btn-dark{display:inline-block;width:74px;height:32px;line-height:32px;font-size:10px;margin-top:8px}
.arrow{position:absolute}

/* hotline */
.hotline{left:0;top:1715px;width:1200px;height:83px;background:var(--charcoal);color:var(--white)}
.hotline .label{position:absolute;left:348px;top:27px;font-size:20px;font-weight:600}
.hotline svg{position:absolute;left:596px;top:24px}
.hotline .num{position:absolute;left:656px;top:17px;font-size:32px;font-weight:600;letter-spacing:1px}

/* gallery */
.gallery{left:0;top:1798px;width:1200px;height:329px;background:var(--mist)}
.gallery .section-title{position:absolute;left:96px;top:38px;color:var(--ink)}
.shot{position:absolute;top:102px;width:162px;height:162px;border-radius:50%;border:5px solid var(--charcoal);transform:translateX(-50%)}
.date{position:absolute;right:-14px;top:-18px;width:64px;height:64px;border-radius:50%;background:var(--orange);color:var(--white);text-align:center;font-size:12px;font-weight:700;line-height:15px;padding-top:15px;border:3px solid var(--white)}

/* testimonials + news */
.col-title{font-size:17px;font-weight:700;color:var(--ink);text-transform:uppercase}
.divider{left:691px;top:2165px;width:1px;height:240px;background:#bbbbbb}
.avatar{left:76px;top:2230px;width:108px;height:108px;border-radius:50%;border:4px solid var(--charcoal);background:linear-gradient(160deg,#c24a5a,#6b2a2a)}
.quote-badge{left:146px;top:2222px;width:40px;height:40px;border-radius:50%;background:var(--orange);color:var(--white);font-size:34px;font-weight:700;text-align:center;line-height:48px}
.t-name{left:231px;top:2232px;font-size:22px;font-weight:600;color:var(--ink)}
.t-name span{font-size:12px;font-weight:400;margin-left:10px}
.t-text{left:231px;top:2270px;width:420px;font-size:12px;line-height:19px;text-align:justify}
.more{font-size:11px;color:var(--body)}
.more b{color:var(--orange);margin-left:6px}
.pager{top:2385px;width:18px;height:18px;background:var(--charcoal)}
.news{left:739px;width:420px;padding-left:69px}
.news .day{position:absolute;left:0;top:4px;width:40px;height:40px;border:1px solid var(--orange);text-align:center;font-size:11px;font-weight:700;color:var(--orange);line-height:17px}
.news .day i{display:block;font-style:normal;background:var(--orange);color:var(--white);font-size:9px}
.news h4{font-size:11px;line-height:15px;font-weight:700;color:var(--orange);text-transform:uppercase}
.news p{margin-top:5px;font-size:10.5px;line-height:17px}
.news .more{margin-top:8px;line-height:15px}

/* footer */
.footer{left:0;top:2456px;width:1200px;height:231px;background:var(--charcoal-soft);color:var(--white)}
.footer .brand-small{position:absolute;left:90px;top:22px;font-size:22px;font-weight:700;line-height:1.1;color:var(--orange)}
.footer .brand-small small{display:block;font-size:12px;letter-spacing:2px}
.footer h5{position:absolute;left:90px;top:106px;font-size:17px;font-weight:400}
.footer address{position:absolute;left:90px;top:143px;font-style:normal;font-size:15px;line-height:25px}
.field{position:absolute;background:#e2e2e2;color:#555;font-size:12px;padding:3px 8px}
.send{position:absolute;left:336px;top:159px;width:80px;height:27px;line-height:27px;background:var(--orange);color:var(--white);font-size:12px;text-align:center}
.social{position:absolute;top:69px;width:54px;height:54px;border-radius:50%;background:var(--white)}
</style>
</head>
<body>

<section class="abs hero" role="img" aria-label="Soft-focus photo of smiling children lying head to head in a circle"></section>
<div class="abs hero-shade"></div>
<div class="abs brand">Pelora Vantu<small>Child Care</small></div>
<nav class="abs nav">
  <a class="current" style="left:56px">Home</a>
  <a style="left:170px">About Us</a>
  <a style="left:291px">News</a>
  <a style="left:406px">Calendar</a>
  <a style="left:544px">Resources</a>
  <a style="left:694px">Photo Gallery</a>
  <a style="left:829px">More</a>
  <a style="left:952px">Contact Us</a>
</nav>

<div class="abs showcase">
  <div class="photo lead-photo" role="img" aria-label="Teacher helping a young boy with building blocks at a table">
    <p>Enroll now!<br>Amazing minds at work</p>
  </div>
  <div class="photo tile t1" role="img" aria-label="Teacher clapping with a toddler"><span>CARE</span></div>
  <div class="photo tile t2" role="img" aria-label="Smiling children in a classroom"><span>LEARNING</span></div>
  <div class="photo tile t3" role="img" aria-label="Boy with glasses at a desk"><span>EDUCATION</span></div>
  <div class="photo tile t4" role="img" aria-label="Girl painting a picture"><span>FUN</span></div>
</div>

<h2 class="abs welcome-title">Welcome to Pelora Vantu Child Care</h2>
<p class="abs welcome-text">Pelora Vantu Daycare has 2 full-time openings for ages 2 to 12 years. We are open Monday- Friday with flexible hours. Occasional after hours or weekend care. We have a wonderful preschool program (Little Lantern Time) which is a professionally designed preschool curriculum that nurtures the whole child and supports the child's social, emotional and intellectual growth with themed units and daily reports home that we do during the school year (September-June). We also offer an afterschool program, with a bus stop one driveway away that serves Harlow Brook Elementary. We have homework help &amp; daily art projects. Our summer program is loads of fun, too!</p>
<div class="abs btn-dark welcome-btn">Read More</div>
<div class="abs welcome-photo" role="img" aria-label="Two children peeking around a tall stack of books"></div>

<section class="abs programs">
  <h2 class="section-title">Program Resources</h2>
  <div class="prog" style="left:186px">
    <h3>Ignoring Misbehavior</h3>
    <div class="pic" role="img" aria-label="Child reading with a parent" style="background:linear-gradient(150deg,#d7c4b0,#3d6aa8)"></div>
    <p>This is an effective way to deal with fighting siblings and misbehavior which is directed at getting attention. Children do need attention and it is important that you give a child your attention at other times and, in particular, when they are behaving well.</p>
    <span class="btn-dark">Read More</span>
  </div>
  <div class="prog" style="left:463px">
    <h3>Encouragement</h3>
    <div class="pic" role="img" aria-label="Children drawing at a table" style="background:linear-gradient(150deg,#e0b98f,#7a8f4e)"></div>
    <p>Many persons spend a lot of time correcting bad behavior. When children are behaving well, they deserve parental attention and appreciation. They will learn that good behavior is a way to be noticed.</p>
    <span class="btn-dark">Read More</span>
  </div>
  <div class="prog" style="left:730px">
    <h3>Time-outs</h3>
    <div class="pic" role="img" aria-label="Grandparent talking with a child" style="background:linear-gradient(150deg,#cfc2b4,#8a6a52)"></div>
    <p>A time-out may be used to separate fighting children or calm an over excited child. The parent calmly explains to the child/children that they must sit quietly for five minutes.</p>
    <span class="btn-dark">Read More</span>
  </div>
  <div class="prog" style="left:999px">
    <h3>Using positives</h3>
    <div class="pic" role="img" aria-label="Happy children sitting together" style="background:linear-gradient(150deg,#f0c98a,#c2523c)"></div>
    <p>Tell children what you want them to do rather than what you do not want them to do. Changing "Don'ts" to "Do's" takes practice but is worth the effort. "Do's" give good ideas rather than bad ones and are more easily understood.</p>
    <span class="btn-dark">Read More</span>
  </div>
  <svg class="arrow" style="left:20px;top:188px" width="18" height="50" viewBox="0 0 18 50"><polyline points="16,2 3,25 16,48" fill="none" stroke="#fff" stroke-width="2"/></svg>
  <svg class="arrow" style="left:1162px;top:188px" width="18" height="50" viewBox="0 0 18 50"><polyline points="2,2 15,25 2,48" fill="none" stroke="#fff" stroke-width="2"/></svg>
</section>

<section class="abs hotline">
  <span class="label">HOT LINE FOR PARENTS</span>
  <svg width="36" height="36" viewBox="0 0 36 36"><circle cx="18" cy="18" r="16" fill="none" stroke="#fff" stroke-width="2"/><path d="M12 10c1-1 2-1 3 0l2 3c.5 1 0 2-1 2.5 1 2.5 3 4.5 5.5 5.5.5-1 1.5-1.5 2.5-1l3 2c1 1 1 2 0 3-2 2-5 2-9-1.5S10 13 12 10z" fill="#fff"/></svg>
  <span class="num">1 800 555 0142</span>
</section>

<section class="abs gallery">
  <h2 class="section-title">Photo Gallery</h2>
  <div class="shot" role="img" aria-label="Children smiling together" style="left:179px;background:linear-gradient(150deg,#f0c070,#c05030)"><div class="date">10<br>April '14</div></div>
  <div class="shot" role="img" aria-label="Girl at a classroom desk" style="left:448px;background:linear-gradient(150deg,#c9b48f,#6e8040)"><div class="date">23<br>July '13</div></div>
  <div class="shot" role="img" aria-label="Teacher reading with a child" style="left:712px;background:linear-gradient(150deg,#e6cdb0,#9a7a5e)"><div class="date">10<br>April '14</div></div>
  <div class="shot" role="img" aria-label="Children playing with toys" style="left:1019px;background:linear-gradient(150deg,#f3d59a,#d27a3c)"><div class="date">23<br>July '13</div></div>
  <svg class="arrow" style="left:20px;top:160px" width="18" height="50" viewBox="0 0 18 50"><polyline points="16,2 3,25 16,48" fill="none" stroke="#e8781e" stroke-width="2"/></svg>
  <svg class="arrow" style="left:1162px;top:160px" width="18" height="50" viewBox="0 0 18 50"><polyline points="2,2 15,25 2,48" fill="none" stroke="#e8781e" stroke-width="2"/></svg>
</section>

<h3 class="abs col-title" style="left:94px;top:2164px">Testimonials</h3>
<div class="abs avatar" role="img" aria-label="Portrait of a parent"></div>
<div class="abs quote-badge">&ldquo;</div>
<div class="abs t-name">Maren<span>(Satisfied Mom)</span></div>
<p class="abs t-text">Our toddler has blossomed since spending time at Pelora Vantu Childcare. He loves attending, and I know he feels well cared for and stimulated. We are very pleased with all he has learned. Tessa provides a wonderful environment, making learning fun. She is caring, kind, and the kids adore her. I would definitely recommend this daycare to anyone.</p>
<div class="abs more" style="left:231px;top:2377px">Read More <b>&raquo;</b></div>
<svg class="abs pager" style="left:608px" width="18" height="18" viewBox="0 0 18 18"><rect width="18" height="18" fill="#333"/><polyline points="11,4 6,9 11,14" fill="none" stroke="#fff" stroke-width="2"/></svg>
<svg class="abs pager" style="left:631px" width="18" height="18" viewBox="0 0 18 18"><rect width="18" height="18" fill="#333"/><polyline points="7,4 12,9 7,14" fill="none" stroke="#fff" stroke-width="2"/></svg>
<div class="abs divider"></div>

<h3 class="abs col-title" style="left:732px;top:2156px">Latest News</h3>
<div class="abs news" style="top:2204px">
  <div class="day">20<i>NOV</i></div>
  <h4>Why knot?</h4>
  <p>I've been thinking about the upcoming school year where for the first time my two youngest daughters will be in different schools.</p>
  <div class="more">Read More <b>&raquo;</b></div>
</div>
<div class="abs" style="left:739px;top:2292px;width:420px;border-top:1px dashed #bbb"></div>
<div class="abs news" style="top:2306px">
  <div class="day">20<i>NOV</i></div>
  <h4>Video post type vestibulum</h4>
  <p>Lorem ipsum dolor sit amet, consectetur adipiscing elit. Curabitur euismod enim ametus adipiscing aliquam.</p>
  <div class="more">Read More <b>&raquo;</b></div>
</div>

<footer class="abs footer">
  <div class="brand-small">Pelora Vantu<small>Child Care</small></div>
  <h5>Contact</h5>
  <address>27 Fennel Hollow Road<br>Alder Bay, OR 97099.</address>
  <div class="field" style="left:336px;top:54px;width:197px;height:23px">Name</div>
  <div class="field" style="left:564px;top:54px;width:197px;height:23px">Email Address</div>
  <div class="field" style="left:336px;top:92px;width:425px;height:50px">Message</div>
  <div class="send">SEND</div>
  <div class="social" style="left:826px"></div>
  <div class="social" style="left:895px"></div>
  <div class="social" style="left:969px"></div>
  <div class="social" style="left:1039px"></div>
</footer>

</body>
</html>
```